Corvane Photography Business Card Design

I need a business card designed for a photography business based in Perth, Western Australia called Corvane Photography.

We specialise in wedding, event photography and portrait photography.

The business card must borrow the style of the attached logo.

The hex codes for the colours in the logo are:
#ED1D85 - Pink
#89C23E - Green
#37282F - Black

The name on the card will be:
Name: Teodric
Phone: 0417360825
Website: www.corvanephotography-example.com.au
Facebook: corvanephotography

I am open and happy to accept creative concepts.

Industry/Entity Type

Business

```html
<!DOCTYPE html>
<html lang="en">
<head>
<meta charset="utf-8">
<title>Corvane Photography Business Card</title>
<link rel="stylesheet" href="https://fonts.googleapis.com/css2?family=Arimo:wght@400;700&family=Tinos&display=swap">
<style>
  :root {
    --pink: #ED1D85;
    --green: #89C23E;
    --black: #37282F;
    --paper: #ffffff;
    --paper-shade: #eeeeee;
    --backdrop: #d9d6d2;
    --text-dark: #37282F;
  }
  * { box-sizing: border-box; margin: 0; padding: 0; }
  html, body {
    width: 1200px;
    height: 1200px;
    overflow: hidden;
    background: var(--backdrop);
  }
  .sheet {
    width: 1200px;
    height: 1200px;
    display: flex;
    flex-direction: column;
    align-items: center;
    justify-content: center;
    gap: 60px;
  }
  .card {
    position: relative;
    width: 900px;
    height: 500px;
    background: radial-gradient(ellipse at 50% 40%, var(--paper) 55%, var(--paper-shade) 100%);
    box-shadow: 0 10px 28px rgba(0,0,0,0.25);
    overflow: hidden;
  }
  .colour-bands {
    position: absolute;
    left: 0; right: 0; bottom: 0;
    height: 14px;
    display: flex;
  }
  .colour-bands .band-pink { flex: 36; background: var(--pink); }
  .colour-bands .band-green { flex: 36; background: var(--green); }
  .colour-bands .band-black { flex: 28; background: var(--black); }

  .brand {
    position: absolute;
    left: 0; right: 0;
    display: flex;
    flex-direction: column;
    align-items: center;
  }
  .brand-mark {
    width: 110px;
    height: 110px;
    border-radius: 50%;
    background: var(--pink);
  }
  .brand-name {
    margin-top: 26px;
    font-family: "Arimo", sans-serif;
    font-weight: 400;
    font-size: 24px;
    letter-spacing: 0.55em;
    text-transform: uppercase;
    color: var(--text-dark);
    padding-left: 0.55em;
  }

  .card-front .brand { top: 50px; }

  .holder-name {
    position: absolute;
    left: 80px;
    top: 350px;
    font-family: "Tinos", serif;
    font-size: 46px;
    color: var(--pink);
  }
  .divider {
    position: absolute;
    left: 330px;
    top: 300px;
    width: 3px;
    height: 140px;
    background: var(--black);
  }
  .contact-list {
    position: absolute;
    left: 360px;
    top: 300px;
    list-style: none;
    display: flex;
    flex-direction: column;
    gap: 18px;
  }
  .contact-item {
    display: flex;
    align-items: center;
    gap: 14px;
    font-family: "Arimo", sans-serif;
    font-size: 23px;
    color: var(--text-dark);
  }
  .contact-item.phone { font-size: 27px; }
  .contact-icon {
    width: 28px;
    height: 28px;
    flex: none;
  }

  .card-back .brand { top: 80px; }
  .web-tag {
    position: absolute;
    left: 50%;
    top: 330px;
    transform: translateX(-50%);
    background: var(--pink);
    padding: 10px 22px;
    font-family: "Arimo", sans-serif;
    font-weight: 700;
    font-size: 24px;
    color: var(--green);
    white-space: nowrap;
  }
</style>
</head>
<body>
<main class="sheet">

  <section class="card card-front" aria-label="Business card front">
    <div class="brand">
      <div class="brand-mark" aria-hidden="true"></div>
      <div class="brand-name">Corvane Photography</div>
    </div>

    <div class="holder-name">Teodric</div>
    <div class="divider" aria-hidden="true"></div>

    <ul class="contact-list">
      <li class="contact-item phone">
        <svg class="contact-icon" viewBox="0 0 28 28" aria-hidden="true">
          <circle cx="14" cy="14" r="14" fill="var(--pink)"/>
          <path d="M9.5 7.5c.8-.6 1.7-.4 2.1.4l1.1 2.2c.3.6.1 1.3-.4 1.7l-.8.6c.7 1.6 1.9 2.9 3.5 3.7l.7-.8c.4-.5 1.1-.7 1.7-.4l2.2 1.1c.8.4 1 1.3.4 2.1l-.8 1c-.6.7-1.6 1-2.5.7-4-1.3-7.1-4.4-8.3-8.4-.3-.9 0-1.9.7-2.5z" fill="#fff"/>
        </svg>
        <span>0417360825</span>
      </li>
      <li class="contact-item web">
        <svg class="contact-icon" viewBox="0 0 28 28" aria-hidden="true">
          <circle cx="14" cy="14" r="14" fill="var(--pink)"/>
          <g fill="none" stroke="#fff" stroke-width="1.4">
            <circle cx="14" cy="14" r="7.5"/>
            <ellipse cx="14" cy="14" rx="3.2" ry="7.5"/>
            <line x1="6.5" y1="14" x2="21.5" y2="14"/>
            <line x1="8" y1="10" x2="20" y2="10"/>
            <line x1="8" y1="18" x2="20" y2="18"/>
          </g>
        </svg>
        <span>www.corvanephotography-example.com.au</span>
      </li>
      <li class="contact-item social">
        <svg class="contact-icon" viewBox="0 0 28 28" aria-hidden="true">
          <circle cx="14" cy="14" r="14" fill="var(--pink)"/>
        </svg>
        <span>corvanephotography</span>
      </li>
    </ul>

    <div class="colour-bands" aria-hidden="true">
      <span class="band-pink"></span><span class="band-green"></span><span class="band-black"></span>
    </div>
  </section>

  <section class="card card-back" aria-label="Business card back">
    <div class="brand">
      <div class="brand-mark" aria-hidden="true"></div>
      <div class="brand-name">Corvane Photography</div>
    </div>

    <div class="web-tag">www.corvanephotography-example.com.au</div>

    <div class="colour-bands" aria-hidden="true">
      <span class="band-pink"></span><span class="band-green"></span><span class="band-black"></span>
    </div>
  </section>

</main>
</body>
</html>
```